QTR Business Card

Harborline Capital Partners is a successful and reputable financial services company.Our main services are home loans, commercial loans, vehicle finance and equipment finance. We also do development finance for property developers. Our company is always evolving to always be an industry leader in best financial service practices with access to the largest range of lenders in the country.

We want the business card to reflect our national finance company. Modern, professional corporate image. At the same time the concept of Harborline Capital Partners is that we help build wealth for you but the process for the client is an enjoyable peaceful experience. Not stressful at all .....

Colors to be same as the logo .... gold silver black white as the options

On the reverse side of the card I wanted either just the logo symbol or the logo symbol and text of the logo ....

It could be on a black background ..... or silver or gold .... want it to be quite striking to look at when you first see the card.

On the other side of the card I wanted the following details:

Doran Pelham
Director

0498 372 604

doran@hbcpx.com.au

Po Box 852
Tarrow ACT 2694

www.hbcpx.com.au

ACN 918 264 057 (This can be in very small print and can be in the bottom corner of the card or somewhere not very prominent)
Updates

As requested Ive uploaded the logo file in both .ai and .pdf formats. Please let me know if you need anything else. Thanks

Reason: Still deciding on which design I like best. I will provide individual feedback as well.

```html
<!DOCTYPE html>
<html lang="en">
<head>
<meta charset="utf-8">
<title>Harborline Capital Partners – Business Card</title>
<link rel="stylesheet" href="https://fonts.googleapis.com/css2?family=Cinzel:wght@400;600&family=Lato:wght@400&display=swap">
<style>
  :root {
    --stage: #2b2c2c;
    --card: #121212;
    --gold: #d4ab4c;
    --silver: #b9b9b9;
    --grey-text: #9c9c9c;
  }
  * { box-sizing: border-box; margin: 0; padding: 0; }
  html, body { width: 1200px; height: 800px; overflow: hidden; background: var(--stage); }
  .canvas {
    width: 1200px; height: 800px;
    display: flex; align-items: center; justify-content: center; gap: 50px;
  }
  .card {
    width: 535px; height: 305px;
    background: var(--card);
    border-radius: 14px;
    position: relative;
    box-shadow: 0 12px 30px rgba(0,0,0,.55);
  }
  /* Details side */
  .card--details .mark-circle {
    position: absolute; left: 40px; top: 72px;
    width: 160px; height: 160px; border-radius: 50%;
    background: var(--gold);
  }
  .details {
    position: absolute; left: 240px; top: 46px;
    font-family: "Lato", Arial, sans-serif; color: var(--grey-text);
  }
  .person-name {
    font-family: "Cinzel", Georgia, serif; font-weight: 600;
    color: var(--gold); font-size: 20px; letter-spacing: .5px;
  }
  .person-role { font-size: 12px; margin-top: 2px; }
  .contact-list { list-style: none; margin-top: 16px; font-size: 11px; }
  .contact-list li { display: flex; align-items: center; gap: 8px; margin-bottom: 6px; }
  .contact-list svg { width: 11px; height: 11px; fill: var(--gold); flex: none; }
  .company-name {
    font-family: "Cinzel", Georgia, serif; font-weight: 600;
    color: var(--gold); font-size: 12.5px; margin-top: 16px; letter-spacing: .4px;
  }
  .address { font-style: normal; font-size: 11px; line-height: 1.6; margin-top: 4px; }
  .acn { color: var(--gold); font-size: 10px; margin-top: 16px; letter-spacing: .4px; }

  /* Brand side */
  .card--brand { display: flex; align-items: center; justify-content: center; gap: 22px; }
  .brand-circle { width: 86px; height: 86px; border-radius: 50%; background: var(--silver); flex: none; }
  .brand-name {
    font-family: "Cinzel", Georgia, serif; font-weight: 600;
    color: var(--gold); font-size: 27px; line-height: 1.15; letter-spacing: 1px;
  }
</style>
</head>
<body>
<main class="canvas">
  <section class="card card--details" aria-label="Business card, contact side">
    <div class="mark-circle"></div>
    <div class="details">
      <h1 class="person-name">Doran Pelham</h1>
      <p class="person-role">Director</p>
      <ul class="contact-list">
        <li><svg viewBox="0 0 24 24" aria-hidden="true"><path d="M6.6 10.8a15.1 15.1 0 0 0 6.6 6.6l2.2-2.2a1 1 0 0 1 1-.25 11.4 11.4 0 0 0 3.6.57 1 1 0 0 1 1 1V20a1 1 0 0 1-1 1A17 17 0 0 1 3 4a1 1 0 0 1 1-1h3.5a1 1 0 0 1 1 1c0 1.25.2 2.45.57 3.57a1 1 0 0 1-.25 1z"/></svg>0498 372 604</li>
        <li><svg viewBox="0 0 24 24" aria-hidden="true"><path d="M2 5h20v14H2zm2 2v.5l8 5 8-5V7l-8 5z"/></svg>doran@hbcpx.com.au</li>
        <li><svg viewBox="0 0 24 24" aria-hidden="true"><path d="M12 2a10 10 0 1 0 0 20 10 10 0 0 0 0-20zm6.9 9h-3a15 15 0 0 0-1.4-6A8 8 0 0 1 18.9 11zM12 4.1c.9 1.3 1.7 3.7 1.9 6.9h-3.8c.2-3.2 1-5.6 1.9-6.9zM9.5 5a15 15 0 0 0-1.4 6h-3A8 8 0 0 1 9.5 5zM5.1 13h3a15 15 0 0 0 1.4 6A8 8 0 0 1 5.1 13zm6.9 6.9c-.9-1.3-1.7-3.7-1.9-6.9h3.8c-.2 3.2-1 5.6-1.9 6.9zm2.5-.9a15 15 0 0 0 1.4-6h3a8 8 0 0 1-4.4 6z"/></svg>www.hbcpx.com.au</li>
      </ul>
      <p class="company-name">Harborline Capital Partners</p>
      <address class="address">P.O. Box 852<br>Tarrow ACT 2694</address>
      <p class="acn">ACN 918 264 057</p>
    </div>
  </section>

  <section class="card card--brand" aria-label="Business card, brand side">
    <div class="brand-circle"></div>
    <p class="brand-name">Harborline<br>Capital Partners</p>
  </section>
</main>
</body>
</html>
```